依頼概要
・添付させていただきました資料の内容①~⑥をA4サイズにまとめたい。
・文章の内容はそのまま使っていただいても多少変更しても構わない。
・新規顧客訪問した際に簡単に弊社の内容を伝える為のツールとして作成。
・会社のロゴをどこかに入れてほしい
以上になります。
コールセンターのイメージ写真はイメージが湧けばいいので、報告書の部分や文字の部分の変更はお任せします。
入居率は後日、お伝えいたします(確認中)

第一印象がよかったです。

今回は多数の応募をしていただきありがとうございました。

```html
<!DOCTYPE html>
<html lang="ja">
<head>
<meta charset="utf-8">
<title>ひばり不動産 賃貸管理のご案内</title>
<link href="https://fonts.googleapis.com/css2?family=Noto+Sans+JP:wght@400;500;700;900&family=Noto+Serif+JP:wght@600;700;900&display=swap" rel="stylesheet">
<style>
:root{
  --brand-red:#a3161c;
  --brand-red-dark:#7e0f14;
  --accent:#e8731c;
  --gold:#ffd84a;
  --ink:#3a2a22;
  --text:#333;
  --muted:#777;
  --paper:#ffffff;
}
*{box-sizing:border-box;margin:0;padding:0}
html,body{width:849px;height:1200px;overflow:hidden;background:var(--paper)}
body{font-family:"Noto Sans JP",sans-serif;color:var(--text)}
.sheet{position:relative;width:849px;height:1200px;overflow:hidden}

/* header */
.masthead{position:absolute;left:0;top:0;width:100%;height:82px;display:flex;align-items:center;padding-left:70px;gap:14px}
.brand-mark{width:38px;height:38px;background:var(--brand-red);flex:none}
.masthead-name{font-weight:900;font-size:32px;color:var(--ink);letter-spacing:1px}

/* headline band */
.headline-band{position:absolute;left:0;top:82px;width:100%;height:160px;background:linear-gradient(180deg,var(--brand-red),var(--brand-red-dark));color:#fff;text-align:center;font-family:"Noto Serif JP",serif;font-weight:900;padding-top:18px}
.headline-band p{font-size:40px;line-height:62px;letter-spacing:1px;white-space:nowrap}
.headline-band .em{color:var(--gold);font-size:54px}

/* service area */
.service-area{position:absolute;left:0;top:242px;width:100%;height:606px;background:linear-gradient(180deg,#dfe7ee 0%,#f4f6f8 55%,#ffffff 100%)}

.occupancy{position:absolute;left:312px;top:248px;width:226px;height:226px;border-radius:50%;background:#fff;text-align:center;z-index:1}
.occupancy .label{font-family:"Noto Serif JP",serif;font-size:26px;font-weight:600;padding-top:8px}
.occupancy .rate{font-weight:900;color:var(--brand-red);font-size:78px;line-height:1}
.occupancy .rate small{font-size:38px}
.occupancy .tiny{position:absolute;right:28px;top:16px;font-size:8px;color:var(--muted);line-height:1.3;text-align:left}
.occupancy .note{font-size:13px;color:var(--muted);line-height:1.45;margin-top:6px}

.feature{position:absolute;top:390px;width:400px;height:400px;border-radius:50%;background:#fff;border:4px solid var(--accent);text-align:center;z-index:2}
.feature-market{left:14px}
.feature-call{left:438px}
.feature-title{font-family:"Noto Serif JP",serif;font-weight:700;font-size:23px;line-height:36px;color:var(--text);margin-top:58px;white-space:nowrap}
.feature-title .hl{color:var(--accent);font-size:27px}
.feature-photo{position:absolute;left:94px;top:138px;width:204px;height:104px;border-radius:0 0 102px 102px;background:linear-gradient(160deg,#d9d2c4,#8e7d6a)}
.partners{position:absolute;left:0;top:238px;width:100%;font-family:"Noto Serif JP",serif;font-weight:700;font-size:20px;line-height:30px;white-space:nowrap}
.partners .num{color:var(--accent);font-size:40px;line-height:46px;font-family:"Noto Sans JP",sans-serif;font-weight:900}
.partners .num small{font-size:24px}

.call-person{position:absolute;top:140px;width:54px;height:54px;border-radius:50%;background:linear-gradient(160deg,#f3c9a3,#c98a5a)}
.call-label{position:absolute;font-size:12px;font-weight:700;color:var(--ink);line-height:1.35;white-space:nowrap;text-align:center}
.call-hub{position:absolute;left:136px;top:196px;width:116px;height:116px;border-radius:50%;background:var(--brand-red);color:#fff;font-weight:700;font-size:13px;line-height:1.45;display:flex;align-items:center;justify-content:center}
.call-foot{position:absolute;left:262px;top:318px;font-size:9px;color:var(--muted);line-height:1.3;text-align:left}

/* bottom */
.menu-box{position:absolute;left:28px;top:852px;width:395px;height:332px;border:2px solid var(--accent)}
.menu-head{background:var(--accent);color:#fff;font-weight:700;font-size:18px;padding:3px 16px}
.menu-intro{font-size:10px;line-height:1.5;padding:8px 16px 6px}
.menu-table{width:calc(100% - 32px);margin:0 16px;border-collapse:collapse;font-size:11.5px}
.menu-table td{padding:3px 4px;border-bottom:1px dotted #bbb;white-space:nowrap}
.menu-table td:first-child::before{content:"■ ";color:var(--accent)}
.menu-table td:last-child{width:44%}

.company{position:absolute;left:444px;top:852px;width:395px;height:334px}
.company-brand{display:flex;align-items:center;gap:14px}
.company-brand .brand-mark{width:46px;height:46px}
.company-name{font-weight:900;font-size:30px;color:var(--ink);line-height:1.1}
.company-name small{display:block;font-size:16px}
.company-body{display:flex;gap:14px;margin-top:12px}
.storefront{width:170px;height:112px;background:linear-gradient(180deg,#c7d3dd,#9aa7b0)}
.address{font-size:10px;color:var(--muted);margin-top:3px}
.tagline{font-weight:700;font-size:15px;line-height:1.65}
.tel{display:flex;align-items:center;gap:6px;margin-top:6px;color:var(--accent);font-weight:900;font-size:40px;line-height:1.1;white-space:nowrap}
.tel span{font-size:17px;font-weight:700}
.center-note{font-size:13px;font-weight:700;line-height:1.5;margin-top:4px;white-space:nowrap}
</style>
</head>
<body>
<div class="sheet">

  <header class="masthead">
    <div class="brand-mark"></div>
    <div class="masthead-name">ひばり不動産は</div>
  </header>

  <section class="headline-band">
    <p>オーナー様の<span class="em">利益</span>を一番に考え</p>
    <p>賃貸経営をお手伝いします!</p>
  </section>

  <section class="service-area" role="img" aria-label="明るい街並みと空の写真"></section>

  <div class="occupancy">
    <div class="label">入居率</div>
    <div class="tiny">20XX年<br>XX月現在</div>
    <div class="rate">00<small>%</small></div>
    <div class="note">不動産の価値を上げる<br>充実のサポート</div>
  </div>

  <div class="feature feature-market">
    <div class="feature-title">市場の<span class="hl">調査・分析</span><br>を行い、募集条件を設定</div>
    <div class="feature-photo" role="img" aria-label="打ち合わせをするビジネスパーソンと観葉植物の写真"></div>
    <div class="partners">
      <div><span class="num">100<small>社</small></span>以上の</div>
      <div>仲介会社様への</div>
      <div>情報提供・訪問営業</div>
    </div>
  </div>

  <div class="feature feature-call">
    <div class="feature-title"><span class="hl">24時間365日</span>対応の<br>管理専門コールセンター</div>
    <div class="call-person" role="img" aria-label="作業員のイラスト" style="left:70px"></div>
    <div class="call-label" style="left:50px;top:198px">解約防止<br>入居率アップ</div>
    <div class="call-person" role="img" aria-label="入居者のイラスト" style="left:274px"></div>
    <div class="call-label" style="left:258px;top:198px">入居者様の<br>満足度アップ</div>
    <div class="call-hub">ひばり不動産<br>コールセンター</div>
    <div class="call-label" style="left:262px;top:278px">現場対応<br>修理対応</div>
    <div class="call-foot">※一部オーナー様の<br>ご負担あり</div>
  </div>

  <section class="menu-box">
    <div class="menu-head">管理メニュー</div>
    <p class="menu-intro">当社は賃貸管理のプロとして、オーナー様の大切な資産を守り、安定した賃貸経営を全力でサポートいたします。</p>
    <table class="menu-table">
      <tr><td>管理料</td><td>5%～</td></tr>
      <tr><td>24時間365日対応</td><td>250円／戸当たり</td></tr>
      <tr><td>敷金</td><td>オーナー様預り</td></tr>
      <tr><td>募集推進費(広告費)</td><td>物件により異なる</td></tr>
      <tr><td>法定点検</td><td>実費請求</td></tr>
      <tr><td>集金業務</td><td>無料</td></tr>
      <tr><td>更新業務</td><td>無料</td></tr>
      <tr><td>家賃督促</td><td>無料</td></tr>
      <tr><td>退去立会い・敷金精算</td><td>無料</td></tr>
      <tr><td>水漏調査・修理</td><td>実費請求</td></tr>
    </table>
  </section>

  <section class="company">
    <div class="company-brand">
      <div class="brand-mark"></div>
      <div class="company-name"><small>株式会社</small>ひばり不動産</div>
    </div>
    <div class="company-body">
      <div>
        <div class="storefront" role="img" aria-label="店舗外観の写真"></div>
        <div class="address">みどり市東区若葉町1-2-3</div>
      </div>
      <p class="tagline">不動産の売却・購入・<br>資産の相談は<br>ひばり不動産まで!</p>
    </div>
    <div class="tel">
      <svg width="34" height="34" viewBox="0 0 24 24" aria-hidden="true"><path fill="currentColor" d="M6.6 10.8a15.1 15.1 0 0 0 6.6 6.6l2.2-2.2c.3-.3.7-.4 1-.2 1.1.4 2.3.6 3.6.6.6 0 1 .4 1 1V20c0 .6-.4 1-1 1C10.6 21 3 13.4 3 4c0-.6.4-1 1-1h3.5c.6 0 1 .4 1 1 0 1.3.2 2.5.6 3.6.1.3 0 .7-.2 1z"/></svg>
      <span>TEL</span>012-345-6789
    </div>
    <p class="center-note">【みどり相続相談センター】も運営しております。<br>お気軽にお問い合わせください。</p>
  </section>

</div>
</body>
</html>
```